A powerful and attractive professional-looking signage

We need a signage for the office at the door entrance. We are a professional advisory firm that serve corporate clients; hence the signage should concur an image of professionalism and sophistication. We have the logo and the Company's Motto. We are looking at having an elegant and contemporary feel to the design - yet it must be professional and sharp.

Target Market(s)

corporates

Industry/Entity Type

Finance

Colors
ffc214

Requirements
Must have
• an impactful first impression - that conjurs image of professionalism
Should not have
• cartoon

```html
<!DOCTYPE html>
<html lang="en">
<head>
<meta charset="utf-8">
<title>Meridian Counsel — Entrance Signage</title>
<link rel="stylesheet" href="https://fonts.googleapis.com/css2?family=EB+Garamond:wght@500&display=swap">
<style>
  :root {
    --page-bg: #ffffff;
    --card-black: #04080a;
    --brand-blue: #1d6cab;
    --motto-orange: #ec5a28;
    --mark-orange: #f26a2a;
    --fold-white: #ffffff;
    --fold-shade: #8c8c8c;
  }
  * { margin: 0; padding: 0; box-sizing: border-box; }
  html, body {
    width: 1200px;
    height: 675px;
    overflow: hidden;
    background: var(--page-bg);
  }
  .signage {
    position: relative;
    width: 1200px;
    height: 675px;
    font-family: "EB Garamond", Georgia, serif;
  }
  .signage__layer {
    position: absolute;
    inset: 0;
    width: 1200px;
    height: 675px;
  }
  .card-face { fill: var(--card-black); }
  .brand-mark {
    position: absolute;
    left: 84px;
    top: 66px;
    width: 152px;
    height: 152px;
    background: var(--mark-orange);
  }
  .brand-name {
    position: absolute;
    left: 308px;
    top: 92px;
    font-size: 94px;
    font-weight: 500;
    line-height: 1;
    letter-spacing: -1px;
    color: var(--brand-blue);
    white-space: nowrap;
  }
  .motto {
    position: absolute;
    left: 88px;
    top: 540px;
    font-size: 44px;
    font-weight: 500;
    line-height: 1;
    letter-spacing: 16px;
    word-spacing: 22px;
    color: var(--motto-orange);
    white-space: nowrap;
  }
</style>
</head>
<body>
<main class="signage">
  <svg class="signage__layer" viewBox="0 0 1500 843" aria-hidden="true">
    <path class="card-face" d="M25 25 H1475 V318 Q1474 342 1452 348 L700 785 Q660 810 600 818 H25 Z"/>
  </svg>

  <div class="brand-mark" aria-hidden="true"></div>
  <h1 class="brand-name">Meridian Counsel</h1>
  <p class="motto">ALWAYS ON THE SAME PAGE</p>

  <svg class="signage__layer" viewBox="0 0 1500 843" aria-hidden="true">
    <defs>
      <linearGradient id="fold-gradient" gradientUnits="userSpaceOnUse" x1="1100" y1="445" x2="1146" y2="525">
        <stop offset="0" stop-color="var(--fold-white)"/>
        <stop offset="0.55" stop-color="var(--fold-white)"/>
        <stop offset="0.85" stop-color="#d4d4d4"/>
        <stop offset="1" stop-color="var(--fold-shade)"/>
      </linearGradient>
    </defs>
    <path class="page-fold" fill="url(#fold-gradient)"
          d="M1452 348 Q1410 305 1355 305 L850 588 Q790 625 700 785 Z"/>
  </svg>
</main>
</body>
</html>
```